Flyer for our prophetic church event

I need a flyer designed for the launching of our "7 Radiant Harvest Gatherings" event. This event should high light the next 7 Sundays starting on February the 11th, 2018

Event Name:
7 Radiant Harvests

Event Slogan or topic:
Go and tell John ... the blind see, the lame walk, the lepers are cleansed, the deaf hear, the dead are raised,
the poor have the gospel preached to them.

Speaker:
Prophet Marcus Obuya

February 11th
February 18th
February 25th
March 4th
March 11th
March 18th
March 25th

Location:
Talvor Community Center
382 Wendle Street
Portland, ME 04981
United States

Time:
10:00AM - 12:00PM

We welcome you all in the name of Jesus Christ

Contact Info:
Tel:+1(555) 302 1189 - Email:contact@mirovalefold.org - Website: http://velosa.org

Target Market(s)

Young adults

Industry/Entity Type

Church

Font styles to use
Other font styles liked:
• Surprise me, I trust the designers skills

Colors

Designer to choose colors to be used in the design.

Requirements
Must have
• The Velosa logo
• Marcus Obuya's picture
• The
Should not have
• The background of the Marcus Obuya's picture

```html
<!DOCTYPE html>
<html lang="en">
<head>
<meta charset="utf-8">
<title>7 Radiant Harvests Flyer</title>
<link rel="stylesheet" href="https://fonts.googleapis.com/css2?family=Bebas+Neue&family=Kaushan+Script&family=Montserrat:wght@500;600&family=Encode+Sans+Condensed:wght@400;600&display=swap">
<style>
  :root {
    --page-bg: #3a3a3a;
    --paper: #ffffff;
    --orange: #ef5a25;
    --orange-soft: #f38a52;
    --amber: #e3832e;
    --amber-soft: #d9782c;
    --rust: #b4561f;
    --ink: #4a4a4a;
    --dark: #1e1e1e;
    --white: #ffffff;
  }
  * { margin: 0; padding: 0; box-sizing: border-box; }
  html, body { width: 1200px; height: 1200px; overflow: hidden; }
  body { background: var(--page-bg); position: relative; }

  .flyer {
    position: absolute; left: 211px; top: 50px;
    width: 777px; height: 1100px;
    background: var(--paper);
    overflow: hidden;
  }
  .hero-left {
    position: absolute; left: 0; top: 0; width: 444px; height: 617px;
    background: linear-gradient(160deg, var(--orange) 0%, var(--orange-soft) 55%, var(--orange) 100%);
  }
  .hero-right {
    position: absolute; left: 467px; top: 0; width: 310px; height: 617px;
    background: linear-gradient(200deg, var(--amber) 0%, var(--amber-soft) 100%);
  }
  .speaker-photo {
    position: absolute; left: 258px; top: 13px; width: 496px; height: 496px;
    border-radius: 50%;
    border: 3px solid var(--white);
    background: radial-gradient(circle at 55% 40%, #d9d9d9 0%, #8b8b8b 45%, #2a2a2a 75%);
  }

  .brand {
    position: absolute; left: 118px; top: 440px;
    display: flex; align-items: center; gap: 10px;
    color: var(--white);
    font-family: "Montserrat", sans-serif; font-weight: 600; font-size: 34px; line-height: 1; letter-spacing: 1px;
  }
  .brand-dot { width: 14px; height: 14px; border-radius: 50%; background: var(--white); }

  .event-title {
    position: absolute; top: 500px; color: var(--white);
    font-family: "Kaushan Script", cursive; font-size: 64px; line-height: 1.2; white-space: nowrap;
  }
  .event-title--left { left: 106px; }
  .event-title--right { left: 478px; }

  .info { position: absolute; left: 0; width: 100%; text-align: center; white-space: nowrap; }
  .slogan-lead { top: 642px; font-family: "Bebas Neue", sans-serif; font-size: 14px; color: var(--ink); letter-spacing: 0.2px; }
  .slogan-main { top: 664px; font-family: "Bebas Neue", sans-serif; font-size: 32px; color: var(--ink); }
  .speaker-label { top: 702px; font-family: "Kaushan Script", cursive; font-size: 30px; color: var(--orange); }

  .speaker-bar {
    position: absolute; left: 164px; top: 753px; width: 472px; height: 51px;
    background: var(--orange); color: var(--white);
    font-family: "Bebas Neue", sans-serif; font-size: 52px; line-height: 54px; text-align: center;
  }

  .dates { position: absolute; top: 815px; left: 0; width: 100%; height: 52px;
    font-family: "Encode Sans Condensed", sans-serif; font-weight: 600; font-size: 11.5px; color: var(--dark); line-height: 16px; }
  .dates-col { position: absolute; }
  .dates-col--1 { left: 249px; top: 0; }
  .dates-col--2 { left: 373px; top: 6px; line-height: 18px; }
  .dates-col--3 { left: 486px; top: 10px; line-height: 18px; }
  .dates-rule { position: absolute; top: 4px; width: 1px; height: 44px; background: var(--orange); }
  .dates-rule--1 { left: 338px; }
  .dates-rule--2 { left: 451px; }

  .location-label { top: 860px; font-family: "Montserrat", sans-serif; font-weight: 600; font-size: 26px; color: var(--rust); }
  .address { top: 898px; font-family: "Encode Sans Condensed", sans-serif; font-size: 21px; color: var(--dark); }
  .time { top: 931px; font-family: "Montserrat", sans-serif; font-weight: 600; font-size: 23px; color: var(--dark); }
  .time-value { color: var(--orange); font-weight: 500; margin-left: 4px; }
  .time-rule { position: absolute; left: 236px; top: 960px; width: 324px; height: 1px; background: #c9c9c9; }
  .welcome { top: 966px; font-family: "Bebas Neue", sans-serif; font-size: 36px; color: var(--rust); }
  .contact-label { top: 1008px; font-family: "Montserrat", sans-serif; font-weight: 600; font-size: 20px; color: var(--dark); }

  .contact-bar {
    position: absolute; left: 105px; top: 1040px; width: 594px; height: 31px;
    background: var(--amber); color: var(--white);
    font-family: "Encode Sans Condensed", sans-serif; font-weight: 600; font-size: 15px; line-height: 31px; text-align: center;
  }
</style>
</head>
<body>
  <main class="flyer">
    <div class="hero-left" role="img" aria-label="Soft orange backdrop with a faint cross"></div>
    <div class="hero-right" role="img" aria-label="Soft amber backdrop with a faint cross"></div>
    <div class="speaker-photo" role="img" aria-label="Portrait of Prophet Marcus Obuya"></div>

    <div class="brand">
      <span class="brand-dot"></span>
      <span class="brand-name">VELOSA</span>
    </div>

    <h1 class="event-title event-title--left">7 Radiant</h1>
    <div class="event-title event-title--right">Harvests</div>

    <p class="info slogan-lead">Go and tell John ... the blind see, the lame walk, the lepers are cleansed, the deaf hear, the dead are raised,</p>
    <p class="info slogan-main">The poor have the gospel preached to them.</p>
    <p class="info speaker-label">Speaker:</p>
    <div class="speaker-bar">PROPHET MARCUS OBUYA</div>

    <div class="dates">
      <div class="dates-col dates-col--1">February 11th<br>February 18th<br>February 25th</div>
      <span class="dates-rule dates-rule--1"></span>
      <div class="dates-col dates-col--2">March 4th<br>March 11th</div>
      <span class="dates-rule dates-rule--2"></span>
      <div class="dates-col dates-col--3">March 18th<br>March 25th</div>
    </div>

    <p class="info location-label">Location:</p>
    <p class="info address">Talvor Community Center 382 Wendle Street Portland, ME 04981 United States</p>
    <p class="info time">Time: <span class="time-value">10:00AM - 12:00PM</span></p>
    <span class="time-rule"></span>
    <p class="info welcome">We welcome you all in the name of Jesus Christ</p>
    <p class="info contact-label">Contact Info:</p>
    <div class="contact-bar">Tel:+1(555) 302 1189 - Email:contact@mirovalefold.org - Website: http://velosa.org</div>
  </main>
</body>
</html>
```